Redesign of business card for Birchline Mechanical

We are looking for a new design for our business cards for Birchline Mechanical. We are a plumbing & HVAC construction company, operating on the West Coast of Canada and USA. Logo attached.
Industry/Entity Type
Construction - Plumbing & HVAC
Contact Information for Business Card
Name, address, phone numbers, email, website address
Look and feel
Each slider illustrates characteristics of the customer's brand and the style your logo design should communicate.

```html
<!DOCTYPE html>
<html lang="en">
<head>
<meta charset="UTF-8">
<title>Birchline Mechanical – Business Card</title>
<link href="https://fonts.googleapis.com/css2?family=Montserrat:wght@400;700&display=swap" rel="stylesheet">
<style>
  :root {
    --backdrop: #6f6f6f;
    --card: #1a1a1a;
    --card-edge: #2a2a2a;
    --silver: #d9d9d9;
    --silver-soft: #b5b5b5;
    --divider: #8a8a8a;
  }
  * { box-sizing: border-box; margin: 0; padding: 0; }
  html, body {
    width: 1200px; height: 800px; overflow: hidden;
    background: var(--backdrop);
    font-family: "Montserrat", sans-serif;
  }
  .stage {
    width: 1200px; height: 800px;
    display: flex; align-items: center; justify-content: center; gap: 40px;
  }
  .card {
    width: 520px; height: 297px;
    background: var(--card);
    border: 1px solid var(--card-edge);
    border-radius: 22px;
    box-shadow: 0 14px 30px rgba(0,0,0,0.35);
    position: relative;
  }
  .card-front { display: flex; }
  .brand-panel {
    width: 240px; height: 100%;
    display: flex; align-items: center; justify-content: center;
    border-right: 1px solid var(--divider);
    margin: 28px 0; height: calc(100% - 56px);
  }
  .brand-name {
    display: flex; align-items: center; gap: 10px;
    color: var(--silver);
    font-weight: 700; font-size: 17px; letter-spacing: 1px;
    text-transform: uppercase;
  }
  .brand-mark {
    width: 14px; height: 14px; background: var(--silver); flex: none;
  }
  .contact-panel {
    flex: 1; padding: 40px 28px 0 30px; color: var(--silver);
  }
  .person-name { font-weight: 700; font-size: 17px; letter-spacing: 1px; }
  .person-role { font-size: 12px; color: var(--silver-soft); margin-top: 2px; }
  .address { font-size: 12px; line-height: 1.5; color: var(--silver-soft); margin-top: 20px; }
  .contact-list { list-style: none; margin-top: 20px; font-size: 12px; line-height: 1.75; color: var(--silver-soft); }
  .contact-list li { display: flex; align-items: center; gap: 8px; }
  .contact-list svg { width: 11px; height: 11px; flex: none; fill: var(--silver); }
  .card-back { display: flex; align-items: center; justify-content: center; }
  .card-back .brand-name { font-size: 24px; gap: 14px; }
  .card-back .brand-mark { width: 18px; height: 18px; }
</style>
</head>
<body>
<main class="stage">
  <section class="card card-front">
    <div class="brand-panel">
      <div class="brand-name"><span class="brand-mark"></span>Birchline Mechanical</div>
    </div>
    <div class="contact-panel">
      <p class="person-name">MARCUS DELANE</p>
      <p class="person-role">President</p>
      <p class="address">4120 Harbor Crest Way<br>Suite 210, Tustin, CA 92780</p>
      <ul class="contact-list">
        <li><svg viewBox="0 0 24 24"><path d="M6.6 10.8a15 15 0 0 0 6.6 6.6l2.2-2.2c.3-.3.7-.4 1-.2 1.1.4 2.3.6 3.6.6.6 0 1 .4 1 1V20c0 .6-.4 1-1 1A17 17 0 0 1 3 4c0-.6.4-1 1-1h3.5c.6 0 1 .4 1 1 0 1.3.2 2.5.6 3.6.1.3 0 .7-.2 1z"/></svg>1-866-555-0148 Toll Free</li>
        <li><svg viewBox="0 0 24 24"><path d="M6.6 10.8a15 15 0 0 0 6.6 6.6l2.2-2.2c.3-.3.7-.4 1-.2 1.1.4 2.3.6 3.6.6.6 0 1 .4 1 1V20c0 .6-.4 1-1 1A17 17 0 0 1 3 4c0-.6.4-1 1-1h3.5c.6 0 1 .4 1 1 0 1.3.2 2.5.6 3.6.1.3 0 .7-.2 1z"/></svg>213-555-0192</li>
        <li><svg viewBox="0 0 24 24"><path d="M2 5h20v14H2z M2 5l10 8 10-8" fill="none" stroke="#d9d9d9" stroke-width="2.5"/></svg>info@birchlinemech.com</li>
        <li><svg viewBox="0 0 24 24"><circle cx="12" cy="12" r="9" fill="none" stroke="#d9d9d9" stroke-width="2.5"/><path d="M3 12h18M12 3c3 3 3 15 0 18M12 3c-3 3-3 15 0 18" fill="none" stroke="#d9d9d9" stroke-width="2"/></svg>www.birchlinemech.com</li>
      </ul>
    </div>
  </section>
  <section class="card card-back">
    <div class="brand-name"><span class="brand-mark"></span>Birchline Mechanical</div>
  </section>
</main>
</body>
</html>
```